Restaurant Finder Website Design

I need to create a website that will help people find restaurants around a zip code or address.

I would like to have a very clean and simple design. I will need a design for the homepage, that should be very clean and simple to use. its where the users will launch their search. I am thinking something like tavlex like.. big search field with a very clean page where users can create an account or restaurants subscribe to the service.

Also need the design of the search results page, I would like to display a big map with the results and a list on the side or the bottom of the map.

Also need a profile page for the users that sign up to the site.

Mostly what I need are guidelines and color coordinated elements, like a general layout and buttons that work together. I would like to know what the action buttons and elements should look like. Because its going to have some more detail pages.

Target Market(s)

People in general, mainly people that work at an office and have to find a place for lunch every day.

Industry/Entity Type

Restaurant

Number of Pages Required

4 page

Font styles to use
Serif
Sans Serif

Requirements
Must have
• It must be a really simple and clean design but look edgy.

```html
<!DOCTYPE html>
<html lang="en">
<head>
<meta charset="utf-8">
<title>PlateNear – My Account</title>
<link rel="stylesheet" href="https://fonts.googleapis.com/css2?family=Raleway:wght@400;500;600;700&display=swap">
<style>
:root{
  --red:#cc0a0a;
  --navy:#1f2937;
  --ink:#2a2a2a;
  --text:#3d3d3d;
  --muted:#6b6b6b;
  --line:#dcdcdc;
  --panel:#efefef;
  --black:#141414;
}
*{box-sizing:border-box;margin:0;padding:0}
html,body{width:1200px;height:1070px;overflow:hidden;background:#fff}
body{font-family:"Raleway",sans-serif;color:var(--text);position:relative}
.abs{position:absolute}
a{color:inherit;text-decoration:none}

.site-header{left:0;top:0;width:1200px;height:76px;background:linear-gradient(#fff,#f1f1f1);border-bottom:2px solid var(--red)}
.brand{left:161px;top:20px;display:flex;align-items:center;gap:10px;font-size:26px;font-weight:500;color:var(--ink)}
.brand-dot{width:30px;height:30px;border-radius:50%;background:var(--red)}
.search{left:430px;top:18px;width:353px;height:39px;border:1px solid #cfcfcf;background:#fff;font-size:13px;color:#9a9a9a;padding:11px 13px}
.search svg{position:absolute;right:12px;top:11px}
.btn{top:21px;height:31px;font-size:11px;font-weight:700;color:#fff;display:flex;align-items:center;justify-content:center;letter-spacing:.3px}
.btn-login{left:853px;width:81px;background:var(--navy)}
.btn-register{left:942px;width:97px;background:var(--red)}

.hero{left:0;top:76px;width:1200px;height:195px;background:linear-gradient(100deg,#8a5a2a 0%,#c9823a 25%,#5f6f2a 45%,#a8622e 65%,#d9a05a 80%,#7a3a1a 100%)}
.avatar{left:162px;top:127px;width:94px;height:94px;border-radius:50%;background:#f2f2f2;overflow:hidden}
.profile-name{left:273px;top:165px;color:#fff;font-size:14px}

.title-band{left:0;top:271px;width:1200px;height:48px;background:linear-gradient(#f7f7f7,#e4e4e4)}
.page-title{left:161px;top:284px;font-size:20px;font-weight:700;color:var(--red)}
.crumbs{right:162px;top:290px;font-size:11px;display:flex;gap:12px}
.crumbs span+span{border-left:1px solid #ccc;padding-left:12px;color:var(--red)}

.side-title{left:161px;top:346px;font-size:18px;font-weight:600;color:var(--ink)}
.side-nav{left:161px;top:381px;width:210px;border-top:2px solid var(--ink);border-left:1px solid var(--line);border-right:1px solid var(--line);list-style:none}
.side-nav li{height:39.8px;border-bottom:1px solid var(--line);display:flex;align-items:center;padding-left:16px;font-size:11px;font-weight:700;color:var(--ink)}
.side-nav li::before{content:"";border-left:4px solid currentColor;border-top:3px solid transparent;border-bottom:3px solid transparent;margin-right:6px}
.side-nav li.active{color:var(--red)}

.main{left:393px;top:346px;width:646px}
.main h2{font-size:18px;font-weight:600;color:var(--ink);padding-bottom:12px;border-bottom:1px solid var(--line)}
.hello{margin-top:17px;font-size:13px;font-weight:700;color:var(--ink)}
.hello span{color:var(--red)}
.intro{margin-top:4px;font-size:12px;line-height:17px}
.sec-head{display:flex;align-items:center;gap:8px;font-size:16px;font-weight:600;color:var(--ink);padding-bottom:10px;border-bottom:1px solid var(--line)}
.sec-head .more{margin-left:auto;font-size:11px;font-weight:500;color:var(--text)}
.cards{display:flex;justify-content:space-between;margin-top:17px}
.card{width:311px;border:1px solid var(--line);position:relative}
.card-head{height:30px;background:var(--panel);display:flex;align-items:center;gap:7px;padding-left:16px;font-size:14px;font-weight:600;color:var(--ink)}
.row{height:42px;display:flex;align-items:center;padding-left:16px;gap:8px;font-size:12px;border-bottom:1px solid var(--line)}
.row:last-child{border-bottom:0}
.edit{position:absolute;right:13px;bottom:13px;font-size:11px;color:var(--red);display:flex;gap:4px;align-items:center}
.addr{padding:14px 18px 30px;font-size:12px;line-height:17px}
.addr strong{display:block;font-size:13px;font-weight:600;color:var(--ink);margin-bottom:3px}

.footer{left:0;top:960px;width:1200px;height:75px;background:var(--red);color:#fff}
.foot-links{left:162px;top:15px;font-size:12px;font-weight:700;display:flex;gap:7px}
.follow{left:163px;top:42px;display:flex;align-items:center;gap:7px;font-size:13px;font-weight:700}
.social{width:21px;height:21px;border-radius:50%;background:#fff}
.foot-brand{right:168px;top:20px;display:flex;align-items:center;gap:10px;font-size:25px;font-weight:500}
.foot-brand .brand-dot{background:#fff}
.legal{left:0;top:1035px;width:1200px;height:35px;background:var(--black);color:#e6e6e6;font-size:11px}
.legal .copy{position:absolute;left:162px;top:11px}
.legal .terms{position:absolute;right:162px;top:11px;display:flex;gap:14px}
.legal .terms span+span{border-left:1px solid #444;padding-left:14px}
</style>
</head>
<body>
<header class="site-header abs">
  <div class="brand abs"><span class="brand-dot"></span>PlateNear</div>
  <div class="search abs">Zip Code or Address
    <svg width="15" height="15" viewBox="0 0 15 15"><circle cx="6" cy="6" r="4.6" fill="none" stroke="#888" stroke-width="2"/><path d="M9.5 9.5L13.5 13.5" stroke="#888" stroke-width="2.2"/></svg>
  </div>
  <a class="btn btn-login abs">LOGIN</a>
  <a class="btn btn-register abs">REGISTER</a>
</header>

<div class="hero abs" role="img" aria-label="Close-up photo of grilled shrimp with peppers, rice and lime"></div>
<div class="avatar abs">
  <svg width="94" height="94" viewBox="0 0 94 94"><circle cx="47" cy="31" r="16" fill="#c8c8c8"/><rect x="15" y="52" width="64" height="50" rx="12" fill="#c8c8c8"/></svg>
</div>
<div class="profile-name abs">Mr. Arlo Venner</div>

<div class="title-band abs"></div>
<h1 class="page-title abs">My Account</h1>
<div class="crumbs abs"><span>Home</span><span>My Account</span></div>

<h3 class="side-title abs">My Account</h3>
<ul class="side-nav abs">
  <li class="active">ACCOUNT DASHBOARD</li>
  <li>ACCOUNT INFORMATION</li>
  <li>ADDRESS BOOK</li>
  <li>MY ORDERS</li>
  <li>BILLING AGREEMENTS</li>
  <li>RECURRING PROFILES</li>
  <li>MY PRODUCT REVIEWS</li>
  <li>MY TAGS</li>
  <li>WISHLIST</li>
  <li>MY APPLICATIONS</li>
  <li>NEWSLETTER SUBSCRIPTIONS</li>
  <li>MY DOWNLOADABLE PRODUCTS</li>
</ul>

<main class="main abs">
  <h2>My Dashboard</h2>
  <p class="hello">Hello, <span>Plate Near</span></p>
  <p class="intro">From your My Account Dashboard you have the ability to view a snapshot of your recent account activity and update your account information. Select a link below to view or edit information.</p>

  <div class="sec-head" style="margin-top:24px">
    <svg width="21" height="16" viewBox="0 0 21 16"><path d="M0 2h8l2 2h11v12H0z" fill="var(--red)"/><circle cx="10.5" cy="8.5" r="2" fill="#fff"/><path d="M7 13c0-2 7-2 7 0z" fill="#fff"/></svg>
    Account Information
  </div>
  <div class="cards">
    <div class="card" style="height:156px">
      <div class="card-head"><svg width="15" height="14" viewBox="0 0 15 14"><path d="M1 5c0-3 13-3 13 0l-3 1c0-2-7-2-7 0z" fill="var(--red)"/><rect x="3" y="7" width="9" height="6" rx="2" fill="var(--red)"/><circle cx="7.5" cy="10" r="1.5" fill="#fff"/></svg>Contact Information</div>
      <div class="row"><svg width="10" height="11" viewBox="0 0 10 11"><circle cx="5" cy="3" r="2.6" fill="#999"/><path d="M0 11c0-5 10-5 10 0z" fill="#999"/></svg>Brightline Works</div>
      <div class="row"><svg width="11" height="8" viewBox="0 0 11 8"><rect width="11" height="8" fill="#999"/><path d="M0 0l5.5 4L11 0" stroke="#fff" fill="none"/></svg>hello@brightlineworks.net &nbsp;- Change Email</div>
      <div class="row"><svg width="10" height="10"><circle cx="5" cy="5" r="5" fill="#999"/></svg>Change Password</div>
      <span class="edit"><svg width="11" height="11" viewBox="0 0 11 11"><rect x=".5" y="2" width="8" height="8.5" fill="none" stroke="var(--red)"/><path d="M4 7l6-6" stroke="var(--red)" stroke-width="1.6"/></svg>Edit</span>
    </div>
    <div class="card" style="height:156px">
      <div class="card-head"><svg width="16" height="14" viewBox="0 0 16 14"><path d="M0 5l8-5 8 5v9H0z" fill="var(--red)"/><path d="M0 5l8 5 8-5" stroke="#fff" fill="none"/></svg>Newsletters</div>
      <div class="row" style="border:0">You are currently subscribed to 'General Subscription'.</div>
      <span class="edit"><svg width="11" height="11" viewBox="0 0 11 11"><rect x=".5" y="2" width="8" height="8.5" fill="none" stroke="var(--red)"/><path d="M4 7l6-6" stroke="var(--red)" stroke-width="1.6"/></svg>Edit</span>
    </div>
  </div>

  <div class="sec-head" style="margin-top:27px">
    <svg width="15" height="16" viewBox="0 0 15 16"><rect x="1" y="1" width="12" height="14" rx="2" fill="none" stroke="var(--red)" stroke-width="1.6"/><circle cx="7" cy="6" r="2" fill="var(--red)"/><path d="M3.5 11.5c0-3 7-3 7 0z" fill="var(--red)"/></svg>
    Address Book<span class="more">Manage Addresses</span>
  </div>
  <div class="cards">
    <div class="card" style="height:162px">
      <div class="card-head"><svg width="12" height="15" viewBox="0 0 12 15"><rect x=".8" y=".8" width="10.4" height="13.4" fill="none" stroke="var(--red)" stroke-width="1.5"/><path d="M3 4h6M3 7h6M3 10h6" stroke="var(--red)"/></svg>Billing Details</div>
      <div class="addr"><strong>Plate Near</strong>48, Cedar Court, Near Lorem Vale,<br>Consequtw, Gohnbrg - 123456<br>Dollortado<br>MORFXD</div>
      <span class="edit"><svg width="11" height="11" viewBox="0 0 11 11"><rect x=".5" y="2" width="8" height="8.5" fill="none" stroke="var(--red)"/><path d="M4 7l6-6" stroke="var(--red)" stroke-width="1.6"/></svg>Edit address</span>
    </div>
    <div class="card" style="height:162px">
      <div class="card-head"><svg width="19" height="15" viewBox="0 0 19 15"><rect x="7" y="1" width="8" height="7" fill="var(--red)"/><path d="M0 10h5l4 2h8v3H0z" fill="var(--red)"/></svg>Shipping Details</div>
      <div class="addr"><strong>Plate Near</strong>48, Cedar Court, Near Lorem Vale,<br>Consequtw, Gohnbrg - 123456<br>Dollortado<br>MORFXD</div>
      <span class="edit"><svg width="11" height="11" viewBox="0 0 11 11"><rect x=".5" y="2" width="8" height="8.5" fill="none" stroke="var(--red)"/><path d="M4 7l6-6" stroke="var(--red)" stroke-width="1.6"/></svg>Edit address</span>
    </div>
  </div>
</main>

<footer class="footer abs">
  <nav class="foot-links abs"><span>Home</span>|<span>What's This?</span>|<span>Dish</span>|<span>Places</span>|<span>Blog</span>|<span>Contact Us</span></nav>
  <div class="follow abs">Follow Us :<span class="social"></span><span class="social"></span><span class="social"></span></div>
  <div class="foot-brand abs"><span class="brand-dot"></span>PlateNear</div>
</footer>
<div class="legal abs">
  <span class="copy">© Copyright 2016 Plate Near. | All Rights Reserved</span>
  <span class="terms"><span>Terms Of Use</span><span>Privacy Statements</span></span>
</div>
</body>
</html>
```